K.L. & Associates
Business Card - Stationary
I need double sided standard sized Business Card [3.5" x 2"]
Use fonts that compliment logo and overall design
Professional
K.L. Benning
Principal Broker
48612 W 31st St Suite D200
Glendale, AZ 85912
Direct: 602-555-0147
kl@klbenning.example
www.klhomesale.example
I'm looking for a clean, modern, professional, design. Please make sure to include colors and font to compliment my logo. Include somewhere on the card. (small) Front or Back where ever it looks best.
Verified Asset Broker™,
PROPLINK ID - 81946,
Meridian Gold Asset Certified, Member - FLCOMB, GTUVW
Design to compliment front of card

```html
<!DOCTYPE html>
<html lang="en">
<head>
<meta charset="utf-8">
<title>K.L. &amp; Associates — Stationery Set</title>
<link href="https://fonts.googleapis.com/css2?family=Lato:wght@400;700&display=swap" rel="stylesheet">
<style>
  :root{
    --bg-top:#e4e4e4;
    --bg-bottom:#2a2a2a;
    --paper:#ffffff;
    --ink:#333333;
    --ink-soft:#777777;
    --brand-red:#b3141b;
    --brand-red-dark:#7d0c10;
    --band-dark:#3a3a3a;
    --band-mid:#6b6b6b;
    --rule:#bdbdbd;
    --label:#8a8a8a;
  }
  *{box-sizing:border-box;margin:0;padding:0}
  html,body{width:1200px;height:526px;overflow:hidden}
  body{
    position:relative;
    background:linear-gradient(to bottom,var(--bg-top) 0%,#bdbdbd 45%,var(--bg-bottom) 100%);
    font-family:"Lato",Arial,sans-serif;color:var(--ink);
  }
  .sheet{position:absolute;background:var(--paper);box-shadow:0 3px 10px rgba(0,0,0,.35);overflow:hidden}
  .piece-label{position:absolute;font-size:9px;color:var(--label);letter-spacing:.3px;white-space:nowrap}

  .brand-name{font-family:"Lato",Arial,sans-serif;font-weight:700;color:var(--ink);white-space:nowrap;position:absolute}
  .address-block{position:absolute;font-size:6.5px;line-height:1.5;color:var(--ink-soft);white-space:nowrap}
  .swoosh{position:absolute;left:0;bottom:0;width:100%}

  /* Invoice */
  .invoice{left:7px;top:43px;width:336px;height:466px}
  .invoice .brand-name{left:20px;top:28px;font-size:17px}
  .invoice .address-block{left:236px;top:20px}
  .invoice-bar{position:absolute;left:14px;right:14px;top:72px;height:16px;background:linear-gradient(var(--band-mid),var(--band-dark));color:#fff;font-size:9px;font-weight:700;padding:3px 8px;letter-spacing:1px}
  .invoice-meta{position:absolute;right:18px;top:98px;font-size:6.5px;color:var(--ink-soft);display:flex;gap:8px}
  .invoice-meta span{display:inline-block;border-bottom:1px solid var(--rule);width:46px}
  .bill-to{position:absolute;left:18px;top:116px;width:145px;height:68px;border:1px solid var(--rule);font-size:6.5px;color:var(--ink-soft);padding:4px}
  .line-items{position:absolute;left:18px;top:196px;width:300px;border-collapse:collapse;font-size:6px;color:var(--ink-soft)}
  .line-items th,.line-items td{border:1px solid var(--rule);height:13px;padding:0 3px;text-align:left;font-weight:400}
  .line-items th{background:#f0f0f0}
  .totals{position:absolute;left:218px;top:334px;font-size:6.5px;color:var(--ink-soft);line-height:18px;width:100px}
  .totals div{display:flex;justify-content:flex-end;gap:4px;align-items:center}
  .totals span{display:inline-block;width:48px;border:1px solid var(--rule);height:13px}
  .signature-box{position:absolute;left:18px;top:394px;width:300px;height:52px;border:1px solid var(--rule);font-size:6.5px;color:var(--ink-soft);padding:4px 4px 4px 170px}

  /* Letterhead */
  .letterhead{left:528px;top:48px;width:636px;height:461px}
  .letterhead .address-block{right:24px;top:18px}
  .letterhead .web{position:absolute;left:232px;bottom:10px;font-size:7px;color:#fff;white-space:nowrap}

  /* Envelope */
  .envelope{left:360px;top:115px;width:456px;height:341px;background:none;box-shadow:none;overflow:visible}
  .envelope-flap{position:absolute;left:0;top:0;width:456px;height:48px}
  .envelope-flap .flap-text{position:absolute;width:100%;top:24px;text-align:center;font-size:6px;color:#ccc}
  .envelope-body{position:absolute;left:0;top:48px;width:456px;height:293px;background:var(--paper);box-shadow:0 3px 10px rgba(0,0,0,.35);overflow:hidden}
  .envelope .brand-name{left:20px;top:40px;font-size:15px}
  .envelope-window{position:absolute;left:165px;top:122px;width:165px;height:56px;border:1px solid #cfcfcf;border-radius:4px;background:#f7f7f7}
  .envelope .return-line{position:absolute;left:0;width:100%;bottom:58px;text-align:center;font-size:6px;color:var(--ink-soft)}

  /* Business cards */
  .card{width:276px;height:128px;left:888px}
  .card-front{top:232px}
  .card-front .brand-name{left:12px;top:30px;font-size:11px}
  .card-name{position:absolute;left:150px;top:14px;font-weight:700;font-size:11px;color:var(--brand-red);white-space:nowrap}
  .card-title{position:absolute;left:150px;top:29px;font-size:6px;color:var(--ink-soft);white-space:nowrap}
  .card-front .address-block{left:12px;top:56px;font-size:5.5px}
  .card-front .web{position:absolute;left:150px;top:70px;font-size:5.5px;color:var(--ink);white-space:nowrap}

  .card-back{top:376px}
  .card-back .top-band{position:absolute;left:0;top:0;width:100%;height:32px;background:linear-gradient(var(--band-dark),var(--band-mid))}
  .credentials{position:absolute;left:12px;top:46px;font-size:6px;line-height:1.55;color:var(--ink)}
  .card-back .web{position:absolute;left:0;width:100%;bottom:8px;text-align:center;font-size:5.5px;color:var(--ink-soft)}
</style>
</head>
<body>

<span class="piece-label" style="left:160px;top:29px">Invoice</span>
<section class="sheet invoice">
  <div class="brand-name">K.L. &amp; Associates</div>
  <div class="address-block">2290 Larkspur Rd Unit 4<br>Brookfield, OR 97031<br>Direct: 602-555-0147<br>kl@klbenning.example</div>
  <div class="invoice-bar">INVOICE</div>
  <div class="invoice-meta">Invoice No <span></span> Date <span></span></div>
  <div class="bill-to">To:</div>
  <table class="line-items">
    <tr><th style="width:38px">Quantity</th><th>Description</th><th style="width:38px">Unit</th><th style="width:48px">Amount</th></tr>
    <tr><td></td><td></td><td></td><td></td></tr><tr><td></td><td></td><td></td><td></td></tr>
    <tr><td></td><td></td><td></td><td></td></tr><tr><td></td><td></td><td></td><td></td></tr>
    <tr><td></td><td></td><td></td><td></td></tr><tr><td></td><td></td><td></td><td></td></tr>
    <tr><td></td><td></td><td></td><td></td></tr><tr><td></td><td></td><td></td><td></td></tr>
  </table>
  <div class="totals">
    <div>Subtotal <span></span></div><div>Tax <span></span></div><div>Total Due <span></span></div>
  </div>
  <div class="signature-box">Signature</div>
</section>

<span class="piece-label" style="left:790px;top:29px">Letterhead - 8.5" X 11"</span>
<section class="sheet letterhead">
  <div class="address-block">2290 Larkspur Rd Unit 4<br>Brookfield, OR 97031<br>Direct: 602-555-0147<br>kl@klbenning.example</div>
  <svg class="swoosh" viewBox="0 0 636 60" height="60" preserveAspectRatio="none" aria-hidden="true">
    <path d="M0 20 Q318 -5 636 25 L636 60 L0 60Z" fill="var(--brand-red)"/>
    <path d="M0 28 Q318 8 636 32 L636 60 L0 60Z" fill="var(--band-dark)"/>
  </svg>
  <div class="web">www.klhomesale.example</div>
</section>

<section class="sheet envelope">
  <div class="envelope-flap">
    <svg viewBox="0 0 456 48" width="456" height="48" aria-hidden="true">
      <defs><linearGradient id="flapShade" x1="0" y1="0" x2="0" y2="1"><stop offset="0" stop-color="#555"/><stop offset="1" stop-color="#2b2b2b"/></linearGradient></defs>
      <path d="M40 0 L416 0 L456 48 L0 48Z" fill="url(#flapShade)"/>
    </svg>
    <div class="flap-text">kl@klbenning.example</div>
  </div>
  <div class="envelope-body">
    <div class="brand-name">K.L. &amp; Associates</div>
    <div class="envelope-window"></div>
    <div class="return-line">2290 Larkspur Rd Unit 4 &nbsp;•&nbsp; Brookfield, OR 97031</div>
    <svg class="swoosh" viewBox="0 0 456 50" height="50" preserveAspectRatio="none" aria-hidden="true">
      <path d="M0 18 Q228 -6 456 18 L456 50 L0 50Z" fill="var(--brand-red)"/>
      <path d="M0 26 Q228 6 456 26 L456 50 L0 50Z" fill="var(--paper)"/>
      <path d="M0 34 Q228 16 456 34 L456 50 L0 50Z" fill="var(--brand-red-dark)"/>
    </svg>
  </div>
</section>
<span class="piece-label" style="left:552px;top:466px">Envelope #10 size</span>

<span class="piece-label" style="left:1095px;top:218px">Business Front</span>
<section class="sheet card card-front">
  <div class="brand-name">K.L. &amp; Associates</div>
  <div class="card-name">K.L. BENNING</div>
  <div class="card-title">Principal Broker</div>
  <div class="address-block">2290 Larkspur Rd Unit 4<br>Brookfield, OR 97031<br>Direct: 602-555-0147<br>kl@klbenning.example</div>
  <div class="web">www.klhomesale.example</div>
  <svg class="swoosh" viewBox="0 0 276 30" height="30" preserveAspectRatio="none" aria-hidden="true">
    <path d="M0 12 Q138 0 276 7 L276 30 L0 30Z" fill="var(--brand-red)"/>
    <path d="M0 17 Q138 5 276 12 L276 30 L0 30Z" fill="var(--band-dark)"/>
  </svg>
</section>

<section class="sheet card card-back">
  <div class="top-band"></div>
  <div class="credentials">Verified Asset Broker™<br>PROPLINK ID - 81946<br>Meridian Gold Asset Certified<br>Member - FLCOMB, GTUVW</div>
  <div class="web">www.klhomesale.example</div>
</section>
<span class="piece-label" style="left:1110px;top:509px">Business Back</span>

</body>
</html>
```